Kem7Dex Letterhead

Need a new letterhead for my law firm.
IDENTIFYING INFORMATION BELOW:
Ansel T Brightwater III
Attorney at Law
Address: 4832 Tillbury Rd, Ste 250, Dallas, TX 75204
Phone: 866-402-7183
Fax: 469-583-0271
Email: kem@kem7dex.example
Website: www.kem7dex.example

Colors
0054AA
0677BA
7BADD7
CADEEF
E8F1F8

Requirements
Must have
• Logo needs to be on the letterhead, along with identifying information which is included in the project description.

```html
<!DOCTYPE html>
<html lang="en">
<head>
<meta charset="utf-8">
<title>Kem7Dex Letterhead</title>
<link rel="stylesheet" href="https://fonts.googleapis.com/css2?family=Arimo:ital,wght@0,400;0,700;1,400;1,700&display=swap">
<style>
  :root {
    --backdrop: #c4c4c4;
    --paper: #ffffff;
    --ink: #1c1c1c;
    --ink-soft: #333333;
    --band-dark: #231f20;
    --brand-blue: #0054aa;
    --brand-mid: #0677ba;
    --brand-pale: #cadeef;
  }
  * { box-sizing: border-box; margin: 0; padding: 0; }
  html, body { width: 1200px; height: 1089px; overflow: hidden; }
  body {
    background: var(--backdrop);
    font-family: "Arimo", Arial, sans-serif;
    color: var(--ink);
    position: relative;
  }
  .letterhead {
    position: absolute;
    left: 205px; top: 33px;
    width: 790px; height: 1022px;
    background: var(--paper);
    box-shadow: 0 6px 24px rgba(0,0,0,.18);
    overflow: hidden;
  }
  .brand {
    position: absolute; left: 70px; top: 52px;
    display: flex; align-items: center; gap: 12px;
  }
  .brand-mark { width: 22px; height: 22px; background: var(--brand-blue); }
  .brand-name {
    font-size: 40px; font-weight: 700; letter-spacing: 2px;
    color: var(--ink); text-transform: uppercase;
  }
  .contact {
    position: absolute; right: 48px; top: 58px;
    display: flex; gap: 22px; font-size: 11px; line-height: 17px; font-style: italic;
    color: var(--ink-soft);
  }
  .contact-name { color: var(--brand-mid); font-weight: 700; font-size: 12px; }
  .contact-lines { list-style: none; }
  .contact-lines li { display: flex; align-items: center; gap: 5px; justify-content: flex-end; }
  .contact-lines svg { width: 10px; height: 10px; fill: var(--brand-mid); }
  .letter {
    position: absolute; left: 70px; top: 170px; right: 70px;
    font-size: 14px; line-height: 20px;
  }
  .letter-date { margin-bottom: 18px; }
  .recipient { margin-bottom: 20px; font-style: normal; }
  .recipient-name { font-weight: 700; }
  .letter p { margin-bottom: 10px; text-align: justify; }
  .signature-mark {
    width: 120px; height: 30px; margin: 14px 0 4px;
    background: linear-gradient(90deg, #f2f2f2, #e6e6e6);
  }
  .signer { font-weight: 700; font-size: 16px; }
  .footer-rule {
    position: absolute; left: 70px; right: 70px; bottom: 34px;
    height: 1px; background: var(--brand-pale);
  }
  .footer-band {
    position: absolute; left: 0; right: 0; bottom: 0; height: 14px;
    background: var(--band-dark);
    border-top: 4px solid var(--brand-blue);
  }
</style>
</head>
<body>
  <main class="letterhead">
    <header>
      <div class="brand">
        <span class="brand-mark"></span>
        <span class="brand-name">Kem7Dex</span>
      </div>
      <div class="contact">
        <div class="contact-identity">
          <div class="contact-name">Ansel T Brightwater III</div>
          <div>Attorney at Law</div>
          <div>4832 Tillbury Rd, Ste 250</div>
          <div>Dallas, TX 75204</div>
        </div>
        <ul class="contact-lines">
          <li><svg viewBox="0 0 10 10"><path d="M2 0l2 2-1 1.5c.6 1.4 1.6 2.4 3 3L7.5 5.5l2 2-1.5 2C4 9 1 6 .5 2z"/></svg>866-402-7183</li>
          <li><svg viewBox="0 0 10 10"><rect x="2" y="0" width="6" height="3"/><rect x="0" y="3.5" width="10" height="4" rx="1"/><rect x="2" y="7" width="6" height="3"/></svg>469-583-0271</li>
          <li><svg viewBox="0 0 10 10"><path d="M0 1h10v8H0z M1 2l4 3 4-3" fill="var(--brand-mid)" stroke="#fff" stroke-width=".8"/></svg>kem@kem7dex.example</li>
          <li><svg viewBox="0 0 10 10"><circle cx="5" cy="5" r="5"/><path d="M0 5h10M5 0c-2 3-2 7 0 10M5 0c2 3 2 7 0 10" stroke="#fff" stroke-width=".7" fill="none"/></svg>www.kem7dex.example</li>
        </ul>
      </div>
    </header>

    <section class="letter">
      <div class="letter-date">4th September 20XX</div>
      <address class="recipient">
        <div class="recipient-name">Ronny Reader</div>
        <div>CEO, Company Name</div>
        <div>123 Address St</div>
        <div>Anytown, ST 12345</div>
      </address>
      <p>Dear Mr. Reader,<br>Lorem ipsum dolor sit amet, consectetuer adipiscing elit, sed diam nonummy nibh euismod tincidunt ut laoreet dolore magna aliquam erat volutpat. Ut wisi enim ad minim veniam, quis nostrud exerci tation ullamcorper suscipit lobortis nisl ut aliquip ex ea commodo consequat.</p>
      <p>Duis autem vel eum iriure dolor in hendrerit in vulputate velit esse molestie consequat, vel illum dolore eu feugiat nulla facilisis at vero eros et accumsan.</p>
      <p>Nam liber tempor cum soluta nobis eleifend option congue nihil imperdiet doming id quod mazim placerat facer possim assum. Typi non habent claritatem insitam; est usus legentis in iis qui facit eorum claritatem. Investigationes demonstraverunt lectores legere me lius quod ii legunt saepius.</p>
      <p>Sincerely,</p>
      <div class="signature-mark" role="img" aria-label="Handwritten signature"></div>
      <div class="signer">Your Name</div>
    </section>

    <div class="footer-rule" aria-hidden="true"></div>
    <div class="footer-band" aria-hidden="true"></div>
  </main>
</body>
</html>
```